Tolvik cards

I want a simple business card that pops.
Logo on one side.
On side two i want.
"Are you thinking about a new building on your property, or renovating an existing structure? Contact".....
Owners Name: Gary Pellman
Owners Phone number: 555-209-4176
Address:4716 Copper Fern RD, Ashgrove, PA 16940
Committed to Quality, Service, and Integrity

```html
<!DOCTYPE html>
<html lang="en">
<head>
<meta charset="utf-8">
<title>Tolvik Builders – Business Cards</title>
<link rel="stylesheet" href="https://fonts.googleapis.com/css2?family=Roboto:wght@400;700;900&family=Poppins:wght@300;600&display=swap">
<style>
  :root {
    --bg: #e4e5e7;
    --card: #ffffff;
    --ink: #3a2512;
    --ink-soft: #5a3d22;
    --rule: #9a7a5a;
  }
  * { margin: 0; padding: 0; box-sizing: border-box; }
  html, body { width: 1200px; height: 800px; overflow: hidden; }
  body {
    background: var(--bg);
    font-family: "Roboto", Arial, sans-serif;
    color: var(--ink);
    display: flex;
    align-items: center;
    justify-content: center;
    gap: 44px;
  }
  .card {
    width: 536px;
    height: 306px;
    background: var(--card);
    box-shadow: 0 10px 28px rgba(0,0,0,0.12), 0 2px 4px rgba(0,0,0,0.06);
    position: relative;
  }

  /* wordmark */
  .wordmark { display: flex; align-items: center; gap: 12px; }
  .wordmark-square { width: 34px; height: 34px; background: var(--ink); flex: none; }
  .wordmark-text {
    font-weight: 900;
    color: var(--ink);
    line-height: 0.9;
    text-transform: uppercase;
  }
  .wordmark-name { display: block; font-size: 58px; letter-spacing: 1px; }
  .wordmark-sub { display: block; font-size: 19px; letter-spacing: 1.5px; margin-top: 4px; }

  /* front */
  .card-front {
    display: flex;
    flex-direction: column;
    align-items: center;
    justify-content: center;
    gap: 26px;
  }
  .front-question {
    font-size: 16px;
    line-height: 1.35;
    text-align: center;
    color: var(--ink-soft);
  }

  /* back */
  .card-back {
    display: grid;
    grid-template-columns: 1.2fr 1px 1fr;
    align-items: center;
    padding: 0 22px;
  }
  .brand-side { display: flex; flex-direction: column; align-items: center; gap: 22px; }
  .brand-side .wordmark-name { font-size: 44px; }
  .brand-side .wordmark-sub { font-size: 15px; }
  .brand-side .wordmark-square { width: 26px; height: 26px; }
  .tagline { font-size: 12px; color: var(--ink-soft); text-align: center; white-space: nowrap; }
  .divider { width: 1px; height: 150px; background: var(--rule); }
  .contact-side { padding-left: 26px; }
  .owner-name {
    font-family: "Poppins", Arial, sans-serif;
    font-size: 27px;
    color: var(--ink);
    margin-bottom: 16px;
    white-space: nowrap;
  }
  .owner-first { font-weight: 600; }
  .owner-last { font-weight: 300; }
  .contact-row { display: flex; align-items: flex-start; gap: 9px; font-size: 13.5px; line-height: 1.3; margin-bottom: 8px; white-space: nowrap; }
  .contact-icon { width: 15px; height: 15px; flex: none; margin-top: 1px; }
</style>
</head>
<body>

<section class="card card-front">
  <div class="wordmark">
    <span class="wordmark-square"></span>
    <span class="wordmark-text">
      <span class="wordmark-name">Tolvik</span>
      <span class="wordmark-sub">Builders LLC</span>
    </span>
  </div>
  <p class="front-question">Are you thinking about a new building on your property,<br>or renovating an existing structure?</p>
</section>

<section class="card card-back">
  <div class="brand-side">
    <div class="wordmark">
      <span class="wordmark-square"></span>
      <span class="wordmark-text">
        <span class="wordmark-name">Tolvik</span>
        <span class="wordmark-sub">Builders LLC</span>
      </span>
    </div>
    <p class="tagline">Committed to Quality, Service, and Integrity</p>
  </div>
  <div class="divider"></div>
  <div class="contact-side">
    <h1 class="owner-name"><span class="owner-first">Gary</span> <span class="owner-last">Pellman</span></h1>
    <div class="contact-row">
      <svg class="contact-icon" viewBox="0 0 16 16" aria-hidden="true">
        <circle cx="8" cy="8" r="8" fill="var(--ink)"/>
        <path d="M5.2 4.2l1.4-.3.8 1.9-.9.7c.5 1 1.2 1.8 2.2 2.3l.7-.9 1.9.8-.3 1.4c-3.2.1-5.9-2.6-5.8-5.9z" fill="#fff"/>
      </svg>
      <span>555-209-4176</span>
    </div>
    <div class="contact-row">
      <svg class="contact-icon" viewBox="0 0 16 16" aria-hidden="true">
        <circle cx="8" cy="8" r="8" fill="var(--ink)"/>
        <path d="M8 3.5a2.8 2.8 0 0 0-2.8 2.8c0 2.1 2.8 5.2 2.8 5.2s2.8-3.1 2.8-5.2A2.8 2.8 0 0 0 8 3.5z" fill="#fff"/>
        <circle cx="8" cy="6.3" r="1" fill="var(--ink)"/>
      </svg>
      <span>4716 Copper Fern RD,<br>Ashgrove, PA 16940</span>
    </div>
  </div>
</section>

</body>
</html>
```